Monthly Newsletter Design template required for Health Business

A newsletter template needs to be created for a health business (dietetic services). The template is to have a banner for the business logo (attached). The newsletter is to be 2 pages with the following parts that will change each month:
Health News
Recipe
Nutrient of the Month
Diet Tweak
Myth Buster
Exercise of the Month
Advertisement / Offer
The design should include heading and paragraph font styles. Recipe and Exercise of the Month will require images to be added.
Updates

Target Market(s)

Newsletter will be sent to clients of the health business (dietetic service)

Industry/Entity Type

Health Service

Requirements
Must have
• 1 X A4 PDF page 1 and page 2 that will form the 2 pages. The newsletter will be electronic and not printed.

```html
<!DOCTYPE html>
<html lang="en">
<head>
<meta charset="utf-8">
<title>Monthly Newsletter – Page 2</title>
<link rel="stylesheet" href="https://fonts.googleapis.com/css2?family=Kaushan+Script&family=Caveat:wght@400;500&family=Crimson+Text:ital,wght@0,400;0,700;1,400&family=Open+Sans:wght@600;700&display=swap">
<style>
  :root {
    --paper: #ffffff;
    --frame: #3a3a3a;
    --ink: #1d1d1b;
    --green-band: #7bc178;
    --recipe-yellow: #fdf26e;
    --exercise-blue: #daeef3;
    --exercise-red: #d92b30;
    --offer-peach: #fbe0d6;
    --offer-red: #d3202f;
    --offer-text: #3d8ed8;
    --accent-orange: #f04e23;
  }
  * { box-sizing: border-box; margin: 0; padding: 0; }
  html, body { width: 848px; height: 1200px; overflow: hidden; background: var(--paper); }
  .page {
    position: relative;
    width: 848px; height: 1200px;
    background: var(--paper);
    border: 1px solid var(--frame);
    color: var(--ink);
    overflow: hidden;
  }
  .nutrient {
    position: absolute; left: 50px; top: 50px; width: 746px; height: 51px;
    background: var(--green-band);
    padding: 2px 4px;
  }
  .nutrient__title {
    font-family: "Kaushan Script", cursive; font-weight: 400;
    font-size: 21px; line-height: 24px;
  }
  .nutrient__text {
    font-family: "Crimson Text", serif; font-size: 15px; line-height: 18px;
    white-space: nowrap; overflow: hidden;
  }
  .recipe {
    position: absolute; left: 490px; top: 106px; width: 306px; height: 636px;
    background: var(--recipe-yellow);
    padding: 2px 4px;
    font-family: "Caveat", cursive; font-size: 14.2px; line-height: 20.2px;
  }
  .recipe__title {
    font-family: "Kaushan Script", cursive; font-weight: 400;
    font-size: 37px; line-height: 44px; text-align: center;
  }
  .recipe__label { margin-top: 0; }
  .recipe__block + .recipe__block { margin-top: 20px; }
  .exercise {
    position: absolute; left: 52px; top: 366px; width: 419px; height: 614px;
    background: var(--exercise-blue);
    padding: 0 2px;
    font-family: "Crimson Text", serif; font-size: 14.6px; line-height: 18.3px;
  }
  .exercise__title {
    font-family: "Open Sans", sans-serif; font-weight: 700;
    color: var(--exercise-red); font-size: 30px; line-height: 40px; text-align: center;
  }
  .exercise__step strong { font-weight: 700; }
  .offer {
    position: absolute; left: 50px; top: 992px; width: 746px; height: 148px;
    background: var(--offer-peach);
    text-align: center; padding: 2px 20px;
  }
  .offer__title {
    font-family: "Kaushan Script", cursive; font-weight: 400;
    color: var(--offer-red); font-size: 29px; line-height: 34px;
  }
  .offer__text {
    font-family: "Caveat", cursive; color: var(--offer-text);
    font-size: 14px; line-height: 19.5px;
  }
  .page-number {
    position: absolute; left: 0; top: 1083px; width: 50px; height: 28px;
    background: var(--accent-orange); color: var(--paper);
    font-family: "Crimson Text", serif; font-size: 19px; line-height: 28px; text-align: center;
  }
  .tip-bar {
    position: absolute; left: 0; top: 1150px; width: 848px; height: 50px;
    background: var(--accent-orange); color: var(--paper);
    font-family: "Open Sans", sans-serif; font-weight: 600;
    font-size: 18px; line-height: 50px; text-align: center;
  }
</style>
</head>
<body>
<main class="page">
  <section class="nutrient">
    <h2 class="nutrient__title">Nutrient of the Month</h2>
    <p class="nutrient__text">Ebis mossi cuptis rem quia consequam, sit estius magni ut et ipsusam quaspic tescid maiosto et quam su</p>
  </section>

  <section class="recipe">
    <h2 class="recipe__title">Recipe</h2>
    <div class="recipe__block">
      <p class="recipe__label">Ingridients:</p>
      <p>Pudam vent pratur? Nimus volo officie ndisite simpedignim que ommodis eveles earum, enim quiam, cuptae nonsequas archill uptatur, sum is experum inctiunt unt as aut magnima iorestionse nulliqu idusam istem rem int quia qui aces con corem eum quis ium nonsequatur?</p>
    </div>
    <div class="recipe__block">
      <p class="recipe__label">Procedure:</p>
      <p>Ur sequo venet autempore nonsero consequam velibusae dolut que cusae ne exeres ute nam, int ressit volum acitist ea vendiorit, sincitate volo quaepudae veratinctem simus. Runt aut omnim cum vent.</p>
      <p>Ra quundit, consed ut ratiae qui doluptas inum rehenda escisq uatquamento volent odia voleste pernam, et, sum reprae non rest pedisci mpost, nobit, culpa dolupitem voloreprae sit que pelestiume venit faciatiuri adisque vel expercit arum quos conet et as susapitem et exceprorrum eumque omnienis dolest eturia cusae. Rum quasit volo venderspe optatec ulparum faccull ate cullecatur ressin eos et andaest ruptatem et audit, sitenis doles dolorruptur, omnihicide net earum qui comnim qui conessuntiam esserum volupta temporp oreniss intotat accuptate numque ducit fugitat apellupid quo ilitini ssinctaturis restrun tionsequi beribusciunt ma voluptaquodi volore millandunt vent volorerum dolore verrovidel il moloria natur ant alis aliquiscil eaquo et lab ipsanderibus conseritaquo min niati asperfe rferecil im qui ut eosam venimpor aut od mod excea consequi dolese secepe lam faccull iquodi consed essite vel moloribus si ipsam dolor sae debis magnist hari.</p>
    </div>
  </section>

  <section class="exercise">
    <h2 class="exercise__title">Exercise of the Month</h2>
    <p class="exercise__step"><strong>Step 1:</strong> Iquodit, omnitisint quibusa conseque vid magnatias remquate nobis est volum dolo quo imus, eiur raepersped mil is que ium facerspissit estota pe nes corem volloru mquibus elit modi aut quae ad ulloribus qui occumet urernat emporrunte ommosap ererio.</p>
    <p class="exercise__step"><strong>Step 2:</strong> At est, erspis ut adipsaperum nulluptaeped earum restis id qui volorpos ma cusaepu dipsandam eos dolecescit faccabo rumqui sequis molorpor saperfe rumque nes etur sentota epudae periat is apeditibus dolupta quidis ent, ommoditaecto doluptur sequasp edipsaersped ut re conseditat veniste sum que eos dis ium harcillo excerum earum cuptaqui cum expliti volut quatem lamendametur sum nullaut am et omnim doloris aut quame veriore perferi qui doluptius accullia culpa prae.</p>
    <p class="exercise__step"><strong>Step 3:</strong> Olum natem susdaest doluptu sandae est, alis provit il ipsa iumquo magnamus, corem et, officipit pores nonsent emolore aut optati totatur?</p>
    <p class="exercise__step"><strong>Step 4:</strong>Rum quia cone saperia vel ipiet, tem que expero te paritasit hitat.Udis et offic to vitat et ento officat earciur?<br>Igene et il is estiae nobiscil mi, omnis dusa delit faccum harum latus.</p>
    <p class="exercise__step"><strong>Step 5:</strong> Ci dis arume pro officia corro quas aut ma consequ oditem di tor abo. Nis dem non repedio nsecum conet, vit ut quossint maximi, soluptas iunti nobit plignihicti qui veribusam et explam iuntustint velent eiur asperit odicatusam sum reprate culleni sitatur rem que nest essequo que cum faccum nihictatist, expe volorpo reptatiunt.</p>
  </section>

  <section class="offer">
    <h2 class="offer__title">Advertisement / Offer</h2>
    <p class="offer__text">Int, tem volor ad moloribus rerrum faceper iaecto idererum alitas doloreius, cum nienditatem quia comniet aut vel magnat.<br>Id quasped quaeptas endae etus imagnis ped eos ad quiatur aut as sum nonecti onecest rundis ducia vitaquis aut estions ectiunt ditissi receaptame vit alitian dellesto venihitatet, autem qui ut dicab inis sintur?<br>Rovit velignias a quaspit aut labo. Et et faccum ipiducit alites ut labo. Utecea voluptat.<br>Occus, serchil litibus volum alitatem rem estrum cum aut ut alis doloresequia et omnimaion exerunte natur?</p>
  </section>

  <div class="page-number">2</div>
  <footer class="tip-bar">Quote or Tips you’d like to hightlight</footer>
</main>
</body>
</html>
```